Healthy Meal Delivery Website Needs to be updated, current, fresh and modern

Hi there,

The current website i have is super old and outdated.

I would like a beautiful modern site that has all the same content as the previous except with a a new, modern and trustworthy feel.

The current website is https://pelvarobistro.com/

Target Market(s)

Health Conscious Young Professionals

Industry/Entity Type

Food Service

Font styles to use
Sans Serif

Requirements
Must have
• Modern Trustworthy feel
Should not have
• Anything out dated or cheesy or scammy

```html
<!DOCTYPE html>
<html lang="en">
<head>
<meta charset="utf-8">
<title>Pelvaro Bistro – Fresh Diet Meals Delivered</title>
<link href="https://fonts.googleapis.com/css2?family=Montserrat:wght@400;600;700;800&family=Open+Sans:wght@400;600&display=swap" rel="stylesheet">
<style>
:root{
  --blue:#2aa8e0;
  --blue-deep:#1f8fcf;
  --yellow:#e6e81e;
  --dark:#2b2b2b;
  --ink:#222;
  --muted:#666;
  --panel:#ececec;
  --line:#dcdcdc;
  --white:#fff;
  --star:#e8552f;
}
*{box-sizing:border-box;margin:0;padding:0}
html,body{width:1200px;height:3974px;overflow:hidden}
body{font-family:'Open Sans',sans-serif;color:var(--ink);background:var(--white);position:relative}
.abs{position:absolute}
.heading{font-family:'Montserrat',sans-serif}

/* header */
.topbar{top:0;left:0;width:1200px;height:85px}
.brand{font-family:'Montserrat',sans-serif;font-weight:700;font-size:22px;color:var(--blue-deep);display:flex;align-items:center;gap:10px}
.brand .dot{width:30px;height:30px;background:var(--yellow);border-radius:50%}
.topbar .brand{left:132px;top:26px}
.contact-item{top:28px;display:flex;gap:12px;align-items:flex-start}
.contact-item .lbl{font-size:10px;font-weight:600;color:var(--ink);letter-spacing:.5px}
.contact-item .val{font-size:15px;color:var(--blue-deep);font-weight:600}
.follow{left:978px;top:28px;font-size:10px;font-weight:600}
.follow .icons{display:flex;gap:10px;margin-top:6px}
.follow .icons span{width:12px;height:12px;background:var(--dark);border-radius:2px}

.nav{top:85px;left:0;width:1200px;height:35px;background:var(--blue)}
.nav ul{list-style:none;display:flex;position:absolute;left:132px;top:0;height:35px}
.nav li{font-family:'Montserrat',sans-serif;font-size:11px;font-weight:700;color:var(--white);padding:0 26px;line-height:35px}
.nav li.active{background:var(--white);color:var(--blue-deep)}
.nav li.signup{background:var(--yellow);color:var(--dark);margin-left:14px}
.nav li.login{background:var(--dark);color:var(--white)}

.hero{top:120px;left:0;width:1200px;height:510px;background:linear-gradient(120deg,#8a6a4a 0%,#c9a176 35%,#6f8f3a 55%,#b23a2c 75%,#5a4030 100%)}
.hero-title{left:138px;top:352px;font-family:'Montserrat',sans-serif;font-weight:800;font-size:52px;line-height:52px;color:var(--white);letter-spacing:1px}
.hero-sub{left:142px;top:522px;background:#1e1e1e;color:var(--white);font-size:15px;font-weight:600;padding:9px 16px}
.slide-arrow{width:38px;height:38px;background:rgba(0,0,0,.55);top:338px;display:flex;align-items:center;justify-content:center}

/* features */
.intro{top:694px;left:132px;width:284px;height:432px;background:var(--yellow);padding:56px 30px}
.intro h2{font-family:'Montserrat',sans-serif;font-weight:400;font-size:24px;line-height:28px;color:var(--ink)}
.intro h2 b{font-weight:700}
.intro p{font-size:13px;line-height:19px;margin-top:22px;color:#333}
.btn{display:inline-block;font-family:'Montserrat',sans-serif;font-weight:700;font-size:11px;padding:11px 22px;border-radius:4px}
.btn-blue{background:var(--blue-deep);color:var(--white)}
.btn-yellow{background:var(--yellow);color:var(--dark)}
.intro .btn{margin-top:28px}
.features{top:694px;left:416px;width:652px;height:432px;background:var(--panel)}
.feature{width:220px}
.feature h3{font-family:'Montserrat',sans-serif;font-size:12px;font-weight:700;margin:14px 0 10px}
.feature p{font-size:11px;line-height:17px;color:#444}

/* diet */
.section-title{width:1200px;text-align:center;font-family:'Montserrat',sans-serif;font-weight:700;font-size:24px}
.section-sub{width:1200px;text-align:center;font-size:14px;color:#333}
.bowl{left:437px;top:1350px;width:331px;height:505px;background:radial-gradient(ellipse at 50% 40%,#d9352b 0%,#5f9b2e 40%,#a8c46a 65%,#f4f4f4 85%);border-radius:48% 48% 40% 40%}
.point{width:300px;display:flex;gap:16px}
.point .leaf{flex:none;width:36px;height:20px}
.point h4{font-family:'Montserrat',sans-serif;font-size:12px;font-weight:700;margin-bottom:8px}
.point p{font-size:11px;line-height:17px;color:#444}
.divider{height:1px;background:var(--line)}

/* menu */
.menu{top:1980px;left:0;width:1200px;height:596px;background:linear-gradient(135deg,#2aa4df,#1b86cc)}
.menu .section-title,.menu .section-sub{color:var(--white)}
.card{top:2205px;width:254px;height:267px;background:var(--white);box-shadow:0 4px 12px rgba(0,0,0,.15)}
.card .photo{height:172px}
.card h5{font-family:'Montserrat',sans-serif;font-size:12px;font-weight:700;margin:20px 22px 6px}
.card .desc{font-size:11px;color:#444;margin:0 22px}
.card .more{font-family:'Montserrat',sans-serif;font-size:11px;font-weight:700;color:var(--blue-deep);margin:10px 22px}
.chev{font-family:'Montserrat',sans-serif;color:var(--white);font-size:30px;top:2300px}

/* testimonials */
.review{top:2822px;width:302px;height:265px;background:var(--white);box-shadow:0 3px 14px rgba(0,0,0,.12);text-align:center}
.avatar{width:74px;height:74px;border-radius:50%;border:3px solid var(--white);position:absolute;left:114px;top:-28px;box-shadow:0 2px 6px rgba(0,0,0,.2)}
.review .name{font-family:'Montserrat',sans-serif;font-size:10px;font-weight:700;margin-top:60px}
.review .stars{color:var(--star);font-size:12px;letter-spacing:1px}
.review .quote{display:flex;gap:10px;text-align:center;padding:14px 28px 0 20px}
.review .quote span{font-family:Georgia,serif;font-size:44px;color:#ccc;line-height:40px}
.review .quote p{font-size:12px;line-height:19px;color:#444}
.t-chev{color:#aaa;font-size:28px;top:2930px}

/* call to action */
.cta{top:3220px;left:0;width:1200px;height:380px;background:linear-gradient(180deg,#f1f1f1,#e2e2e2)}
.cta h2{font-family:'Montserrat',sans-serif;font-weight:700;font-size:20px}
.cta .lead{font-size:18px;color:#333;margin-top:4px}
.cta p.body{font-size:12px;line-height:19px;color:#444;width:420px;margin:14px auto 0}

/* footer */
.foot-col h6{font-family:'Montserrat',sans-serif;font-size:11px;font-weight:700;color:var(--blue-deep);margin-bottom:14px}
.foot-col li{list-style:none;font-size:11px;line-height:16px;color:#333}
.foot-row{display:flex;gap:12px;font-size:11px;color:#333;margin-bottom:14px;align-items:flex-start}
.social{display:flex;gap:12px;align-items:center;font-size:11px;margin-bottom:14px}
.social i{width:26px;height:26px;border-radius:50%;display:block}
</style>
</head>
<body>

<header class="abs topbar">
  <div class="abs brand"><span class="dot"></span>Pelvaro Bistro</div>
  <div class="abs contact-item" style="left:570px">
    <svg width="16" height="16" viewBox="0 0 24 24"><path fill="#1f8fcf" d="M6.6 10.8a15 15 0 0 0 6.6 6.6l2.2-2.2a1 1 0 0 1 1-.25 11.4 11.4 0 0 0 3.6.57 1 1 0 0 1 1 1V20a1 1 0 0 1-1 1A17 17 0 0 1 3 4a1 1 0 0 1 1-1h3.5a1 1 0 0 1 1 1c0 1.25.2 2.45.57 3.57a1 1 0 0 1-.25 1z"/></svg>
    <div><div class="lbl">PHONE</div><div class="val">(555) 214-3090</div></div>
  </div>
  <div class="abs contact-item" style="left:755px">
    <svg width="18" height="14" viewBox="0 0 24 18"><path fill="#1f8fcf" d="M0 0h24v18H0z"/><path fill="none" stroke="#fff" stroke-width="2" d="M1 1l11 9 11-9"/></svg>
    <div><div class="lbl">E-MAIL</div><div class="val">sales@pelvarobistro.com</div></div>
  </div>
  <div class="abs follow">FOLLOW US<div class="icons"><span></span><span></span><span></span></div></div>
</header>

<nav class="abs nav">
  <ul>
    <li class="active">HOME</li><li>PELVARO MEAL PLANS</li><li>MENU</li><li>PRICING</li><li>ABOUT</li><li>PRESS</li><li>CONTACT</li><li class="signup">SIGNUP</li><li class="login">LOGIN</li>
  </ul>
</nav>

<section class="abs hero" role="img" aria-label="Close-up of toasted bread topped with fresh salad greens and cherry tomatoes"></section>
<h1 class="abs hero-title">FRESH<br>DIET MEALS<br>DELIVERED</h1>
<div class="abs hero-sub">Providing Toronto diet meal delivery for 15 years.</div>
<div class="abs slide-arrow" style="left:0"><svg width="10" height="14"><path d="M8 1 2 7l6 6" fill="none" stroke="#fff" stroke-width="2"/></svg></div>
<div class="abs slide-arrow" style="left:1162px"><svg width="10" height="14"><path d="M2 1l6 6-6 6" fill="none" stroke="#fff" stroke-width="2"/></svg></div>

<section class="abs intro">
  <h2>The Pelvaro Diet Delivers <b>Diet Meals To Your Door</b> In Toronto, Gta And Montreal</h2>
  <p>Our fresh and delicious diet meals and snacks are made with only the best natural ingredients that nourish your body. Why not let us prepare your meals while you lose the weight?</p>
  <span class="btn btn-blue">READ MORE</span>
</section>
<section class="abs features">
  <div class="abs feature" style="left:72px;top:40px">
    <svg width="50" height="46" viewBox="0 0 50 46"><path d="M20 4c3 3-3 5 0 8M28 4c3 3-3 5 0 8" stroke="#1f8fcf" stroke-width="2" fill="none"/><path d="M4 20h42a21 21 0 0 1-42 0z" fill="#1f8fcf"/></svg>
    <h3>HEALTHY</h3><p>The Pelvaro Diet is a great way to ensure you are eating all the nutrients you need, and nothing your body doesn't need.</p>
  </div>
  <div class="abs feature" style="left:382px;top:40px">
    <svg width="50" height="46" viewBox="0 0 50 46"><rect x="10" y="6" width="28" height="34" rx="4" fill="#1f8fcf"/><rect x="16" y="14" width="16" height="3" fill="#fff"/><rect x="16" y="22" width="16" height="3" fill="#fff"/></svg>
    <h3>CHOICE</h3><p>You can choose your own meals from over 100 tasty entrees, desserts and snack foods. You can choose your meals online...</p>
  </div>
  <div class="abs feature" style="left:72px;top:230px">
    <svg width="50" height="46" viewBox="0 0 50 46"><path d="M8 40 30 12l8 8z" fill="#1f8fcf"/><path d="M30 12l6-8M34 16l8-4M32 14l10-2" stroke="#1f8fcf" stroke-width="3"/></svg>
    <h3>FRESH</h3><p>All of our meals are real food, freshly prepared by our in-house expert chefs.</p>
  </div>
  <div class="abs feature" style="left:382px;top:230px">
    <svg width="50" height="46" viewBox="0 0 50 46"><path d="M4 22h42a21 21 0 0 1-42 0z" fill="#1f8fcf"/><circle cx="28" cy="12" r="6" fill="#1f8fcf"/></svg>
    <h3>CUSTOMIZED</h3><p>Your meals will be delivered fresh to your door, customized for your unique body type and level of activity.</p>
  </div>
</section>

<h2 class="abs section-title" style="top:1214px;left:0">The Pelvaro Diet</h2>
<p class="abs section-sub" style="top:1256px;left:0">Real foods designed by nature prepared by Pelvaro.</p>

<div class="abs bowl" role="img" aria-label="Fresh vegetables and salad leaves falling into a white bowl"></div>

<div class="abs point" style="left:138px;top:1430px"><svg class="leaf" viewBox="0 0 36 20"><path d="M2 10C8 0 22 0 34 4 26 16 12 20 2 10z" fill="#1f8fcf"/></svg><div><h4>WHAT YOU GET</h4><p>Pelvaro Diet Delivery provides you with 3 fresh daily meals and 3 snacks delivered to your doorstep before 8am.</p></div></div>
<div class="abs divider" style="left:132px;top:1542px;width:300px"></div>
<div class="abs point" style="left:138px;top:1572px"><svg class="leaf" viewBox="0 0 36 20"><path d="M2 10C8 0 22 0 34 4 26 16 12 20 2 10z" fill="#1f8fcf"/></svg><div><h4>SELECTION</h4><p>Choose your meals from over 100 delicious entrees, snacks and desserts.</p></div></div>
<div class="abs divider" style="left:132px;top:1668px;width:300px"></div>
<div class="abs point" style="left:138px;top:1700px"><svg class="leaf" viewBox="0 0 36 20"><path d="M2 10C8 0 22 0 34 4 26 16 12 20 2 10z" fill="#1f8fcf"/></svg><div><h4>LUXURY</h4><p>Enjoy the luxury of having your own personal chef and nutritionist prepare Pelvaro Diet.</p></div></div>

<div class="abs point" style="left:818px;top:1466px"><svg class="leaf" viewBox="0 0 36 20"><path d="M2 10C8 0 22 0 34 4 26 16 12 20 2 10z" fill="#1f8fcf"/></svg><div><h4>WHAT IS PHASE 1?</h4><p>Phase 1 is the stricter phase that eliminates bad carbs and processed foods; no sugar, candy, pasta or bread.</p></div></div>
<div class="abs divider" style="left:768px;top:1582px;width:300px"></div>
<div class="abs point" style="left:818px;top:1610px"><svg class="leaf" viewBox="0 0 36 20"><path d="M2 10C8 0 22 0 34 4 26 16 12 20 2 10z" fill="#1f8fcf"/></svg><div><h4>WHAT IS PHASE 2?</h4><p>Phase 2 reintroduces certain healthy carbs into your diet - whole grains, rice and potatoes, providing you with a greater variety of meals.</p></div></div>

<section class="abs menu">
  <h2 class="abs section-title" style="top:72px;left:0">Select From Over 100 Menu Items</h2>
  <p class="abs section-sub" style="top:126px;left:0;line-height:24px">You can choose your own meals from over 100 tasty entrees, desserts and snack foods.<br>You can choose your meals online, or we can select your meals for you.</p>
</section>
<div class="abs chev" style="left:116px">&#8249;</div>
<div class="abs chev" style="left:1064px">&#8250;</div>
<article class="abs card" style="left:201px"><div class="photo" role="img" aria-label="Buttermilk cinnamon waffles" style="background:linear-gradient(135deg,#c98b45,#8a5424)"></div><h5>BREAKFAST</h5><p class="desc">BUTTERMILK CINNAMON WAFFLES</p><p class="more">READ MORE</p></article>
<article class="abs card" style="left:469px"><div class="photo" role="img" aria-label="Fruit and yogurt parfait with strawberries and grapes" style="background:linear-gradient(135deg,#f3efe6,#e0483a 55%,#f0b43a)"></div><h5>FRUIT AND YOGURT PARFAIT</h5><p class="desc">grapes, strawberries, oranges, mango...</p><p class="more">READ MORE</p></article>
<article class="abs card" style="left:734px"><div class="photo" role="img" aria-label="Berry crepes" style="background:linear-gradient(135deg,#e8c28a,#7a1d2a 60%,#3b2a5a)"></div><h5>BERRY CREPES</h5><p class="desc">flour, eggs, water, salt, olive oil, berries</p><p class="more">READ MORE</p></article>

<div class="abs" role="img" aria-label="Bowl of fresh green salad" style="left:-20px;top:2610px;width:150px;height:240px;border-radius:0 50% 50% 0;background:radial-gradient(circle at 40% 45%,#5c9c2c,#c9372b 55%,#f2f2f2 75%,transparent 76%)"></div>
<h2 class="abs section-title" style="top:2666px;left:0">What They Say</h2>
<div class="abs t-chev" style="left:204px">&#8249;</div>
<div class="abs t-chev" style="left:970px">&#8250;</div>
<article class="abs review" style="left:270px"><div class="avatar" role="img" aria-label="Customer portrait" style="background:#c79a7a"></div><p class="name">MARLA</p><p class="stars">★★★★★</p><div class="quote"><span>“</span><p>I have been very impressed with the food. I've done a few other meal delivery services and yours is by far the best in terms of flavour, freshness and quality.</p></div></article>
<article class="abs review" style="left:615px"><div class="avatar" role="img" aria-label="Customer portrait" style="background:#6d5a50"></div><p class="name">RENATA</p><p class="stars">★★★★★</p><div class="quote"><span>“</span><p>Thanks so much. We had a fabulous day on October 14th. Wedding day physique thanks to Pelvaro!</p></div></article>
<div class="abs" role="img" aria-label="Dried apricots and dates" style="left:1030px;top:3000px;width:170px;height:210px;border-radius:50% 0 0 50%;background:radial-gradient(circle at 60% 50%,#d9761f,#8a3412 55%,transparent 72%)"></div>

<section class="abs cta" role="img" aria-label="Soft grey background photo of fresh salad ingredients">
  <div style="position:absolute;top:88px;left:0;width:1200px;text-align:center">
    <h2>The PELVARO DIET Is Based On Real Foods Made</h2>
    <p class="lead">With Fresh And Natural Ingredients.</p>
    <p class="body">It's about eating the foods you love and emphasizing the ones that nourish your body: generous portions of fresh fruit, vegetables, meat, fish, nuts and seeds, with smaller servings of grains and dairy.</p>
    <div style="margin-top:32px;display:flex;gap:14px;justify-content:center"><span class="btn btn-blue">CUSTOMER LOGIN</span><span class="btn btn-yellow">SIGN UP NOW</span></div>
  </div>
</section>

<footer>
  <div class="abs brand" style="left:160px;top:3720px"><span class="dot"></span>Pelvaro Bistro</div>
  <div class="abs foot-col" style="left:511px;top:3668px;width:200px">
    <h6>CONTACT US</h6>
    <div class="foot-row"><svg width="10" height="14" viewBox="0 0 10 14"><path d="M5 0a5 5 0 0 1 5 5c0 4-5 9-5 9S0 9 0 5a5 5 0 0 1 5-5z" fill="#222"/><circle cx="5" cy="5" r="2" fill="#fff"/></svg><span>118 Harlow Street<br>Brantwood, IL 60199</span></div>
    <div class="foot-row"><svg width="12" height="12" viewBox="0 0 24 24"><path fill="#222" d="M6.6 10.8a15 15 0 0 0 6.6 6.6l2.2-2.2a1 1 0 0 1 1-.25 11.4 11.4 0 0 0 3.6.57 1 1 0 0 1 1 1V20a1 1 0 0 1-1 1A17 17 0 0 1 3 4a1 1 0 0 1 1-1h3.5a1 1 0 0 1 1 1c0 1.25.2 2.45.57 3.57a1 1 0 0 1-.25 1z"/></svg><span>555-214-3090 (3090)</span></div>
    <div class="foot-row"><svg width="12" height="10" viewBox="0 0 24 18"><path fill="#222" d="M0 0h24v18H0z"/><path fill="none" stroke="#fff" stroke-width="2" d="M1 1l11 9 11-9"/></svg><span>sales@pelvarobistro.com</span></div>
  </div>
  <div class="abs foot-col" style="left:747px;top:3668px">
    <h6>MENU</h6>
    <ul><li>HOME</li><li>PELVARO MEAL PLANS</li><li>MENU</li><li>PRICING</li><li>ABOUT</li><li>PRESS</li><li>CONTACT</li><li>SIGN UP</li><li>LOGIN</li></ul>
  </div>
  <div class="abs foot-col" style="left:935px;top:3668px">
    <h6>CONNECT WITH US</h6>
    <div class="social"><i style="background:#3b5998"></i>Friendsheet</div>
    <div class="social"><i style="background:#29a9e0"></i>Chirper</div>
    <div class="social"><i style="background:#0e4f8a"></i>WorkLink</div>
  </div>
  <div class="abs divider" style="left:132px;top:3890px;width:936px"></div>
  <p class="abs" style="left:0;top:3928px;width:1200px;text-align:center;font-size:11px;color:#444">Copyrights @ 2018 All Rights Reserved</p>
</footer>

</body>
</html>
```